Website for Yacht hire/ sailing school business | ||
A new look for an established website | ||
Outdoors | ||
harrowdenesailing.co.uk | ||
The company has been in business for 18 years and operates out of a marina in soutth west Wales. Main activities are: 1) Sailing school, offering courses from beginner to expert both on the water and in the classroom 2) Sailboat charter/hire 3) Adventure Cruises on a skippered boat 4) New Yacht Sales |
Easy to navigate site needed with the emphasis on easy user experience and navigation Needs to be clean, uncluttered yet attractive |
Clean/Simple Content Driven Friendly Exciting Sophisticated Modern Progressive Service Oriented |
page outer background may be #004488 | ||
could be a gradient to #062858 | ||
main content area white | ||

```html
<!DOCTYPE html>
<html lang="en">
<head>
<meta charset="utf-8">
<title>Harrowdene Sailing</title>
<link href="https://fonts.googleapis.com/css2?family=Arimo:wght@400;700&display=swap" rel="stylesheet">
<style>
:root{
  --page-top:#004488;
  --page-bottom:#062858;
  --topbar:#8e1c20;
  --topbar-dark:#5e0f12;
  --white:#ffffff;
  --ink:#444a52;
  --muted:#6b727a;
  --accent:#c4262c;
  --navy:#1b4f86;
  --navy-dark:#123a66;
  --navy-line:#3a6fa5;
  --panel:#dfeaf4;
  --panel-edge:#b8cde0;
  --grey-panel:#eeeeee;
  --grey-edge:#cfcfcf;
}
*{box-sizing:border-box;margin:0;padding:0}
html,body{width:1200px;height:1007px;overflow:hidden}
body{
  font-family:"Arimo",Arial,sans-serif;
  color:var(--ink);
  background:linear-gradient(var(--page-top),var(--page-bottom));
  position:relative;
}
.topbar{
  position:absolute;left:0;top:0;width:1200px;height:46px;
  background:linear-gradient(var(--topbar),var(--topbar-dark));
}
.top-links{position:absolute;right:165px;top:10px;display:flex;gap:26px;font-size:13px}
.top-links a{color:#f3d6d6;text-decoration:none}
.top-links a.current{color:var(--white)}
.site{
  position:absolute;left:169px;top:30px;width:860px;height:912px;
}
.header{position:absolute;left:0;top:0;width:860px;height:84px;background:var(--white);border-radius:6px 6px 0 0}
.brand-tab{
  position:absolute;left:12px;top:-2px;width:300px;height:92px;background:var(--white);
  border-radius:0 0 8px 8px;box-shadow:0 3px 6px rgba(0,0,0,.18);
  display:flex;align-items:center;justify-content:center;gap:10px;
}
.brand-mark{width:18px;height:18px;border-radius:50%;background:var(--navy)}
.brand-name{font-size:22px;font-weight:700;color:var(--navy);letter-spacing:.5px}
.contact{position:absolute;left:420px;top:36px;text-align:right;font-size:11px;color:var(--muted)}
.contact strong{font-size:17px;color:var(--ink)}
.contact .email{color:var(--accent)}
.follow{position:absolute;right:20px;top:22px;border-left:1px solid #ddd;padding-left:14px;font-size:12px;color:var(--navy);font-weight:700}
.follow .icons{display:flex;gap:6px;margin-top:6px}
.follow .icons span{width:22px;height:22px;border-radius:3px;background:#3b74b5}
.follow .icons span+span{background:#3fb2e6}
.main{position:absolute;left:0;top:84px;width:860px;height:828px;background:var(--white);border-radius:0 0 6px 6px}
.side-nav{position:absolute;left:11px;top:0;width:193px;height:281px;background:linear-gradient(var(--navy),var(--navy-dark));border-radius:4px;padding:8px 6px}
.side-nav a{display:block;height:29.5px;line-height:29px;padding-left:16px;font-size:13px;color:#eaf2fb;text-decoration:none;border-bottom:1px solid var(--navy-line);position:relative}
.side-nav a::before{content:"";position:absolute;left:6px;top:12px;border:3px solid transparent;border-left-color:#9fc1e4}
.side-nav a.current{font-weight:700;color:var(--white)}
.hero{position:absolute;left:212px;top:0;width:639px;height:294px;border-radius:4px;overflow:hidden;
  background:linear-gradient(120deg,#b9c9d6 0%,#8da2b4 35%,#2f4e6f 70%,#1b3552 100%)}
.hero-caption{position:absolute;right:10px;bottom:12px;color:var(--white);font-size:22px;text-shadow:0 1px 3px rgba(0,0,0,.6)}
.welcome{position:absolute;left:16px;top:313px;width:528px}
.welcome h1{font-size:24px;font-weight:400;color:#333;margin-bottom:12px}
.welcome h1 span{color:var(--navy)}
.welcome p{font-size:11.5px;line-height:1.5;color:var(--muted)}
.intro-row{display:flex;gap:14px;margin-top:8px}
.badge{width:118px;height:104px;border:1px solid #ccc;background:#f4f6f8;flex:none;position:relative}
.badge::after{content:"";position:absolute;left:18px;top:18px;width:80px;height:68px;background:#2c5d9a;border-radius:4px}
.services{list-style:none;font-size:11.5px;line-height:1.55;color:var(--muted);margin-top:4px}
.services li::before{content:"› ";color:var(--accent)}
.services li.hot{color:var(--accent)}
.more{display:block;margin-top:6px;font-size:11px;font-weight:700;color:var(--accent);text-decoration:none}
.sales{position:absolute;left:560px;top:313px;width:288px;height:239px;background:var(--grey-panel);border:1px solid var(--grey-edge);border-radius:6px;padding:6px}
.sales h2{font-size:15px;color:#444;padding:4px 6px 8px}
.sales-mark{height:80px;background:var(--white);border:1px solid var(--grey-edge);display:flex;align-items:center;justify-content:center;gap:10px}
.sales-mark .dot{width:20px;height:20px;border-radius:50%;background:var(--accent)}
.sales-mark span{font-size:26px;font-weight:700;color:#1f3f6a;letter-spacing:1px}
.sales p{font-size:10.5px;line-height:1.4;color:var(--muted);padding:8px 4px 8px 118px;margin-left:-112px}
.sales p{padding-left:118px}
.quote{display:flex;align-items:center;gap:10px;font-size:11px;color:#555;padding:4px}
.quote strong{display:block;font-size:18px;color:var(--navy)}
.card{position:absolute;top:595px;width:408px;height:232px;background:linear-gradient(var(--panel),#f2f7fb);border:1px solid var(--panel-edge);border-radius:6px}
.card.school{left:16px}
.card.charter{left:440px}
.card .photo{position:absolute;left:8px;top:8px;width:160px;height:214px;border-radius:4px}
.school .photo{background:linear-gradient(#7fa7c7,#4d6f8d 60%,#8b3b35)}
.charter .photo{background:linear-gradient(#8a5a3a,#5a3b28 50%,#9aa6ae)}
.card h3{position:absolute;left:184px;top:10px;font-size:21px;font-weight:400;color:#333}
.card .copy{position:absolute;left:184px;top:44px;width:210px;font-size:10.5px;line-height:1.4;color:var(--muted)}
.card .copy p+p{margin-top:10px}
.card .more{position:absolute;left:184px;bottom:10px}
.footer-nav{position:absolute;left:0;top:942px;width:1200px;text-align:center;font-size:11.5px;color:#c7d7ea}
.footer-nav a{color:#c7d7ea;text-decoration:none;margin:0 9px}
.copyright{position:absolute;left:0;top:968px;width:1200px;text-align:center;font-size:10px;color:#7d97b8}
</style>
</head>
<body>
<div class="topbar">
  <nav class="top-links"><a class="current" href="#">Home</a><a href="#">About Us</a><a href="#">Contact</a><a href="#">Gallery</a><a href="#">Message Board</a></nav>
</div>

<div class="site">
  <header class="header">
    <div class="brand-tab"><span class="brand-mark"></span><span class="brand-name">HARROWDENE SAILING</span></div>
    <div class="contact">CONTACT US: <strong>01632 960500</strong><br>Email: <span class="email">info@harrowdenesailing.co.uk</span></div>
    <div class="follow">Follow Us On:<div class="icons"><span></span><span></span></div></div>
  </header>

  <main class="main">
    <nav class="side-nav">
      <a class="current" href="#">Home</a>
      <a href="#">Sailing Courses</a>
      <a href="#">Cruises</a>
      <a href="#">Yacht Charter</a>
      <a href="#">Shorebased</a>
      <a href="#">Valdoret Yacht Sales</a>
      <a href="#">How To Book</a>
      <a href="#">Training School</a>
    </nav>

    <div class="hero" role="img" aria-label="Sailors on the deck of a yacht at sea">
      <div class="hero-caption">Shorebased Courses</div>
    </div>

    <section class="welcome">
      <h1>Welcome to <span>Harrowdene Sailing</span></h1>
      <p>We are one of the leading NBQ Sailing Schools in the UK offering sailing courses, sailing holidays, UK yacht charter and new Valdoret yacht sales.</p>
      <div class="intro-row">
        <div class="badge" aria-label="Training centre badge"></div>
        <div>
          <ul class="services">
            <li class="hot">SAILING COURSES</li>
            <li>SAILING BREAKS</li>
            <li>YACHT CHARTER</li>
            <li>VALDORET YACHT SALES</li>
          </ul>
          <p style="margin-top:6px">Learn to sail on one of our NBQ sailing courses in the UK's only coastal National Park. With spectacular scenery and wildlife, we guarantee un-crowded sailing, all within a testing tidal environment.</p>
        </div>
      </div>
      <a class="more" href="#">Click for more information ›</a>
    </section>

    <aside class="sales">
      <h2>Valdoret Sales</h2>
      <div class="sales-mark"><span class="dot"></span><span>VALDORET</span></div>
      <p style="padding-left:4px;margin-left:0">The full range of yachts are available from Harrowdene Sailing, supplied by a team dedicated to delivering service, value and your ultimate satisfaction.</p>
      <div class="quote">
        <svg width="30" height="26" viewBox="0 0 30 26"><rect x="1" y="1" width="28" height="18" rx="3" fill="#8a8f95"/><path d="M6 19 L6 25 L12 19 Z" fill="#8a8f95"/><path d="M10 6c1-1 2-1 3 0l1 2-1 1c1 2 2 3 4 4l1-1 2 1c1 1 1 2 0 3-3 2-11-5-10-10z" fill="#fff"/></svg>
        <div>Please Call For a Quote:<strong>01632 960500</strong></div>
      </div>
    </aside>

    <article class="card school">
      <div class="photo" role="img" aria-label="Student at the helm of a sailing yacht"></div>
      <h3>Training School</h3>
      <div class="copy">
        <p>Learn to sail on one of our NBQ sailing courses in the UK's only coastal National Park. With spectacular scenery and wildlife, we guarantee un-crowded sailing, all within a testing tidal environment.</p>
        <p>We provide a full range of sailing courses and sailing...</p>
      </div>
      <a class="more" href="#">Read More ›</a>
    </article>

    <article class="card charter">
      <div class="photo" role="img" aria-label="Cruising yacht moored in a marina"></div>
      <h3>Possible Yacht Charter</h3>
      <div class="copy">
        <p>Learn to sail on one of our NBQ sailing courses in the UK's only coastal National Park. With spectacular scenery and wildlife, we guarantee un-crowded sailing, all within a testing tidal environment.</p>
        <p>We provide a full range of sailing courses and sailing...</p>
      </div>
      <a class="more" href="#">Read More ›</a>
    </article>
  </main>
</div>

<nav class="footer-nav"><a href="#">Home</a>|<a href="#">Sailing Courses</a>|<a href="#">Courses</a>|<a href="#">Yacht Charter</a>|<a href="#">Shorebased</a>|<a href="#">Valdoret Yacht Sales</a>|<a href="#">How To Book</a>|<a href="#">Training School</a></nav>
<div class="copyright">Copyright © 2011 harrowdenesailing.co.uk. All Rights Reserved.</div>
</body>
</html>
```